Eye-catching Card for new church

I would like a card the size of a business card ... that can be used to announce the start of our new church. I would like it to have our logo on the card, my name, and the statement "Coming Soon ... 1.10.2016". I also would like to list our website address and Facebook page and my Twitter account.

Target Market(s)

prospective people looking for a church

Industry/Entity Type

Church

Requirements
Must have
• a focus on Coming Soon ... 1.10.2016
• Brightfield Church logo
Should not have
• church buildings or writings on the cross

```html
<!DOCTYPE html>
<html lang="en">
<head>
<meta charset="utf-8">
<title>Brightfield Church – Coming Soon Card</title>
<link href="https://fonts.googleapis.com/css2?family=Oswald:wght@400;500;600&family=Yanone+Kaffeesatz:wght@400&family=Open+Sans:wght@400;600&display=swap" rel="stylesheet">
<style>
  :root {
    --page-bg: #e6e7ea;
    --card-bg: #ffffff;
    --ink-dark: #3b3d40;
    --ink-grey: #6d6f73;
    --rule-grey: #d4d5d8;
    --brand-blue: #1d6fc4;
    --band-light: #4db5ea;
    --band-deep: #1b4ea6;
  }
  * { box-sizing: border-box; margin: 0; padding: 0; }
  html, body { width: 1200px; height: 900px; overflow: hidden; }
  body {
    background: var(--page-bg);
    display: flex;
    align-items: center;
    justify-content: center;
    font-family: "Open Sans", Arial, sans-serif;
  }
  .announcement-card {
    position: relative;
    width: 460px;
    height: 800px;
    background: var(--card-bg);
    border-radius: 24px;
    overflow: hidden;
    box-shadow: 0 10px 30px rgba(0,0,0,0.12);
    display: flex;
    flex-direction: column;
    align-items: center;
  }
  .brand-block {
    height: 330px;
    width: 100%;
    display: flex;
    align-items: center;
    justify-content: center;
    gap: 14px;
    padding-top: 40px;
  }
  .brand-dot {
    width: 34px;
    height: 34px;
    border-radius: 50%;
    background: var(--ink-dark);
    flex: none;
  }
  .brand-name {
    font-family: "Oswald", Arial, sans-serif;
    font-weight: 600;
    font-size: 36px;
    line-height: 1;
    color: var(--ink-dark);
    white-space: nowrap;
  }
  .notch-rule { width: 84%; height: 18px; display: block; }
  .holder-name {
    margin-top: 26px;
    font-family: "Oswald", Arial, sans-serif;
    font-weight: 600;
    font-size: 38px;
    letter-spacing: -0.5px;
    color: var(--ink-dark);
  }
  .holder-name .holder-accent { color: var(--brand-blue); }
  .thin-rule {
    width: 76%;
    height: 1px;
    background: var(--rule-grey);
  }
  .thin-rule.after-name { margin-top: 22px; }
  .launch-message {
    margin-top: 20px;
    font-family: "Yanone Kaffeesatz", Arial, sans-serif;
    font-size: 50px;
    line-height: 1.08;
    color: var(--brand-blue);
    text-align: center;
  }
  .site-plain {
    margin-top: 14px;
    font-size: 16px;
    color: var(--ink-grey);
  }
  .thin-rule.after-site { margin-top: 16px; }
  .social-handle {
    margin-top: 20px;
    font-size: 17px;
    color: var(--ink-dark);
  }
  .web-band {
    position: absolute;
    left: 0; right: 0; bottom: 0;
    height: 62px;
    background: linear-gradient(90deg, var(--band-light) 0%, var(--band-light) 35%, var(--band-deep) 100%);
    display: flex;
    align-items: center;
    justify-content: center;
    color: #ffffff;
    font-weight: 600;
    font-size: 18px;
    letter-spacing: 0.3px;
  }
</style>
</head>
<body>
  <article class="announcement-card">
    <header class="brand-block">
      <div class="brand-dot"></div>
      <div class="brand-name">BRIGHTFIELD CHURCH</div>
    </header>

    <svg class="notch-rule" viewBox="0 0 400 18" preserveAspectRatio="none" aria-hidden="true">
      <polyline points="0,4 188,4 200,15 212,4 400,4" fill="none" stroke="#b9bbbf" stroke-width="2"/>
    </svg>

    <h1 class="holder-name">YOUR <span class="holder-accent">NAME</span></h1>
    <div class="thin-rule after-name"></div>

    <p class="launch-message">"Coming Soon ...<br>1.10.2016".</p>
    <p class="site-plain">brightfieldchurch.com</p>
    <div class="thin-rule after-site"></div>

    <p class="social-handle">@brightfieldchurch</p>

    <footer class="web-band">www.brightfieldchurch.com</footer>
  </article>
</body>
</html>
```